UPDATED BRIEF: We are looking for a trade show booth design - The design is for 10ft x 10 ft booth curved booth display.
we want to utilize the laptop image more with a half wheel of the key services on our platform.
Strategic DEI Business Partner Workshops
Leader to Leader Training
ERG Leader Strategic Training
15 - Microlearning Labs
Coaching & Mentorship
DEI Research, Articles and Hot topics

With the tagline: Experience the Power of Strategic DEI Training and Peer-to-Peer Support on One Platform

About us: we are a learning and development community for diversity and inclusion and talent management professionals. Our corporate colors are blue, 004AAD
We are looking for a clean, corporate design that makes someone feel included. The moment you look at it, you feel included. We may add a screenshot of the Brightpath Growth Studio platform. Our logo will be included and our tagline is

"Together We Can Create a More Inclusive Future: The Brightpath Growth Studio Community for DEI and Talent Leaders."

We have two versions of our logo - one with text only the other with the logo design. We're not sure which one we want to use.

Target Market(s)

Human Resources and Talent Leaders

Industry/Entity Type

Training and development

Colors
0054AA
0677BA
7BADD7
CADEEF
E8F1F8
F0912C
F2A743
F7CA91
FBE8D2
FDF5EE
EB3D1F
EC4F4E
F09395
F8D3D4
FCEDEE

Requirements
Must have
• Must have logo and good visual design
Should not have
• I've added the examples of what I am looking for

```html
<!DOCTYPE html>
<html lang="en">
<head>
<meta charset="UTF-8">
<title>Brightpath Growth Studio – Trade Show Booth</title>
<link href="https://fonts.googleapis.com/css2?family=Montserrat:wght@500;600;700;800&display=swap" rel="stylesheet">
<style>
  :root{
    --stage:#e6e9ee;
    --brand-blue:#0d4aa8;
    --accent-blue:#0a48b4;
    --navy:#111c43;
    --white:#ffffff;
    --pill-text:#0d4aa8;
    --screen-dark:#1a2233;
    --screen-light:#eef1f6;
  }
  *{box-sizing:border-box;margin:0;padding:0}
  html,body{width:833px;height:1200px;overflow:hidden}
  body{background:var(--stage);font-family:'Montserrat',sans-serif;position:relative}
  .booth{position:absolute;left:20px;top:352px;width:793px;height:496px;background:var(--brand-blue);overflow:hidden;box-shadow:0 6px 24px rgba(0,0,0,.25)}
  .side-panel{position:absolute;top:0;width:74px;height:439px;background:var(--navy)}
  .side-panel.left{left:0}
  .side-panel.right{right:0}
  .side-foot{position:absolute;bottom:0;width:74px;height:57px;background:var(--accent-blue)}
  .side-foot.left{left:0}
  .side-foot.right{right:0}
  .side-url{position:absolute;top:50%;left:50%;white-space:nowrap;color:var(--white);font-size:13px;font-weight:500;letter-spacing:2.2px}
  .side-url b{font-weight:700}
  .left .side-url{transform:translate(-50%,-50%) rotate(-90deg)}
  .right .side-url{transform:translate(-50%,-50%) rotate(90deg)}
  .base-band{position:absolute;left:74px;right:74px;bottom:0;height:57px;background:var(--navy);display:flex;align-items:center;justify-content:center}
  .base-url{color:var(--white);font-size:11px;font-weight:500;letter-spacing:2px}
  .base-url b{font-weight:700}
  .notches{position:absolute;inset:0;pointer-events:none}
  .logo{position:absolute;left:0;right:0;top:26px;text-align:center;color:var(--white);font-weight:800;font-size:30px;line-height:1.1;letter-spacing:1px;text-transform:uppercase}
  .service-wheel{position:absolute;inset:0}
  .pill{position:absolute;width:148px;height:30px;border-radius:15px;background:var(--white);color:var(--pill-text);font-size:7.6px;font-weight:700;letter-spacing:1px;text-transform:uppercase;display:flex;align-items:center;justify-content:center;text-align:center;line-height:1.2}
  .laptop{position:absolute;left:267px;top:141px;width:260px;height:148px}
  .laptop-screen{position:absolute;left:23px;top:0;width:214px;height:138px;border-radius:6px;background:linear-gradient(90deg,var(--screen-dark) 0 27%,var(--screen-light) 27% 100%);border:4px solid #0e0f12}
  .laptop-base{position:absolute;left:0;bottom:0;width:260px;height:10px;border-radius:0 0 10px 10px;background:linear-gradient(#d6d9de,#8d9199)}
  .down-marker{position:absolute;left:390px;top:318px}
  .headline{position:absolute;left:74px;right:74px;top:334px;text-align:center;color:var(--white);font-weight:800;font-size:19.5px;line-height:23px;letter-spacing:1.6px;text-transform:uppercase}
</style>
</head>
<body>
  <section class="booth">
    <div class="side-panel left"><span class="side-url">WWW.<b>BRIGHTPATHGROWTHSTUDIO</b>.COM</span></div>
    <div class="side-panel right"><span class="side-url">WWW.<b>BRIGHTPATHGROWTHSTUDIO</b>.COM</span></div>
    <div class="side-foot left"></div>
    <div class="side-foot right"></div>
    <div class="base-band"><span class="base-url">WWW.<b>BRIGHTPATHGROWTHSTUDIO</b>.COM</span></div>
    <svg class="notches" width="793" height="496" viewBox="0 0 793 496">
      <polygon points="29,439 37,431 45,439" fill="var(--accent-blue)"/>
      <polygon points="748,439 756,431 764,439" fill="var(--accent-blue)"/>
      <polygon points="389,439 397,447 405,439" fill="var(--brand-blue)"/>
    </svg>

    <div class="logo">Brightpath<br>Growth Studio</div>

    <svg class="service-wheel" width="793" height="496" viewBox="0 0 793 496" fill="none" stroke="#fff" stroke-width="1.6">
      <path d="M228 137 Q316 217 228 297"/>
      <path d="M566 137 Q478 217 566 297"/>
      <line x1="240" y1="177" x2="263" y2="177"/>
      <line x1="240" y1="217" x2="272" y2="217"/>
      <line x1="240" y1="257" x2="263" y2="257"/>
      <line x1="531" y1="177" x2="554" y2="177"/>
      <line x1="522" y1="217" x2="554" y2="217"/>
      <line x1="531" y1="257" x2="554" y2="257"/>
      <g fill="var(--brand-blue)">
        <circle cx="228" cy="137" r="4"/><circle cx="263" cy="177" r="4"/><circle cx="272" cy="217" r="4"/><circle cx="263" cy="257" r="4"/><circle cx="228" cy="297" r="4"/>
        <circle cx="566" cy="137" r="4"/><circle cx="531" cy="177" r="4"/><circle cx="522" cy="217" r="4"/><circle cx="531" cy="257" r="4"/><circle cx="566" cy="297" r="4"/>
      </g>
    </svg>

    <div class="pill" style="left:96px;top:162px">Strategic DEI Business<br>Partner Workshops</div>
    <div class="pill" style="left:96px;top:202px">Leader to Leader<br>Training</div>
    <div class="pill" style="left:96px;top:242px">ERG Leader Strategic<br>Training</div>
    <div class="pill" style="left:550px;top:162px">15 - Microlearning<br>Labs</div>
    <div class="pill" style="left:550px;top:202px">Coaching and<br>Mentorship</div>
    <div class="pill" style="left:550px;top:242px">DEI Research, Articles<br>and Hot Topics</div>

    <div class="laptop" role="img" aria-label="Laptop showing the Brightpath Growth Studio community platform screen">
      <div class="laptop-screen"></div>
      <div class="laptop-base"></div>
    </div>

    <svg class="down-marker" width="14" height="8" viewBox="0 0 14 8"><polygon points="0,0 14,0 7,7" fill="#fff"/></svg>

    <h1 class="headline">Experience the power of<br>strategic DEI training &amp; peer-to-peer<br>support on one platform</h1>
  </section>
</body>
</html>
```